依頼詳細
・商品の特徴:現在販売している「牛ホルモン」や「豚コマ切れ」を家庭で使いたい分だけすぐに使用できる個食パックシリーズ(100g×3P)を作ります。
・価格:300円~1000円
・ターゲット層:30代~、小家族、単身者
・販売先:百貨店、デパート、通販、スーパー(ディスカウントショップ除く)

記載項目
・商品種類は10種類以上を予定しています。(バラ・コマ切れ・ぶつ切り・焼肉カットなど)
・デザインは下記の3種類からお選び下さい。
「牛ホルモン」「豚コマ切れ」「とりもも(小)」
・調理例を掲載する場合は添付写真をご利用下さい。
・袋サイズ:W255×H180
・デザインしていただく部分:W255×H180
・材質:PP
・色数:4色(白を含む)
・中身を見て購入して頂きたいので、中身が見える小窓を付けて頂きたいです。
・品名は商品の部位となります。判読性よく、大きめでお願いします。
・商品特徴を記載お願いします。(表現は自由に変更してください。何個でも使用可能です)
①肉屋の
②手軽に
③収納上手
④使い切りサイズ
⑤本格調理
⑥メインディッシュ
⑦新鮮素材
希望イメージ
シンプル 複雑
単色 カラフル
暗い 明るい
日常 高級
遊び心 厳粛
未来的 伝統的
女性的 男性的
希望する色
赤系、茶系、緑系、黄・オレンジ系、グレー系、紫系
納品ファイル
• 高解像度JPG (.jpg)
• イラストレーター形式 (.ai)
補足説明
添付のイメージ写真はあくまでもイメージとなっています。
・シリーズでの販売
・ギフトでも販売可能
・シンプルで簡潔で分かりやすいデザイン
皆さん、ご応募頂き有難うございます。
もう少しデザインを見させて頂きたいため、延長させて下さい。
何卒ご理解の程、宜しくお願い致します。
皆様、デザイン提供有難うございます。
もう少し検討時間を延長させて頂いております。
何卒ご理解の程、宜しくお願い致します。

どのデザインも素晴らしかったのですが、ニーズに沿っており弊社の女性社員投票で1位だったためです。絵も入っており、シンプル且つ可愛さがあり、目を惹くデザインでしたので選ばせて頂きました。

皆さんの素晴らしいデザインには本当に悩みました。最終的に社内投票になったのですが、どれも夢の溢れる商品開発が出来ると感じました。有難うございました。

```html
<!DOCTYPE html>
<html lang="ja">
<head>
<meta charset="utf-8">
<title>個食パックシリーズ パッケージ</title>
<link rel="stylesheet" href="https://fonts.googleapis.com/css2?family=Noto+Serif+JP:wght@500;900&family=Noto+Sans+JP:wght@700;900&family=Pinyon+Script&display=swap">
<style>
  :root{
    --bg:#ffffff;
    --silver-light:#f2f2f2;
    --silver-mid:#d9d9d9;
    --silver-dark:#bdbdbd;
    --window:#c4c4c4;
    --window-edge:#e6e6e6;
    --badge-red:#d4101c;
    --white:#ffffff;
    --ink:#1a1a1a;
    --beef:#4a2b7c;
    --pork:#8c1a2c;
    --chicken:#1e5b3c;
  }
  *{box-sizing:border-box;margin:0;padding:0}
  html,body{width:1200px;height:2404px;overflow:hidden;background:var(--bg)}
  .sheet{position:relative;width:1200px;height:2404px}
  .pack{
    position:absolute;left:20px;width:1160px;height:760px;
    background:linear-gradient(135deg,var(--silver-light),var(--silver-mid) 40%,var(--silver-light) 60%,var(--silver-dark));
    overflow:hidden;
  }
  .pack--beef{top:20px;--theme:var(--beef)}
  .pack--pork{top:822px;--theme:var(--pork)}
  .pack--chicken{top:1624px;--theme:var(--chicken)}
  .pack__frame{position:absolute;inset:18px;border:3px solid var(--theme)}
  .pack__frame::after{content:"";position:absolute;inset:8px;border:2px solid var(--theme)}
  .pack__window{position:absolute;left:280px;top:330px;width:800px;height:360px}
  .pack__header{
    position:absolute;left:290px;top:80px;width:640px;height:400px;
    background:var(--theme);color:var(--white);text-align:center;
    box-shadow:0 0 0 4px rgba(255,255,255,.7);
  }
  .pack__tagline{
    position:absolute;left:40px;top:28px;white-space:nowrap;
    font-family:"Noto Serif JP",serif;font-weight:500;font-size:36px;font-style:italic;
    color:rgba(255,255,255,.9);letter-spacing:2px;
  }
  .pack__animal{
    position:absolute;right:50px;top:20px;width:90px;height:64px;border-radius:10px;
    background:rgba(255,255,255,.55);
  }
  .pack__name{
    position:absolute;left:0;right:0;top:150px;white-space:nowrap;
    font-family:"Noto Sans JP",sans-serif;font-weight:900;font-size:108px;line-height:1;
    letter-spacing:2px;text-shadow:0 4px 0 rgba(0,0,0,.25);
  }
  .pack__name small{font-size:84px;letter-spacing:0}
  .pack__size{
    position:absolute;left:0;right:0;top:296px;white-space:nowrap;
    font-family:"Noto Sans JP",sans-serif;font-weight:700;font-size:38px;
    display:flex;justify-content:center;align-items:center;gap:10px;
  }
  .pack__size-pill{
    background:var(--white);color:var(--badge-red);border-radius:40px;
    padding:0 24px;font-weight:900;
  }
  .pack__series{
    position:absolute;left:70px;top:160px;width:150px;height:150px;border-radius:22px;
    background:var(--badge-red);color:var(--white);border:4px solid var(--white);
    font-family:"Noto Sans JP",sans-serif;font-weight:900;text-align:center;
    display:flex;flex-direction:column;justify-content:center;line-height:1.1;
  }
  .pack__series span{font-size:38px}
  .pack__series em{font-style:normal;font-size:22px;margin-top:6px}
  .pack__spec{
    position:absolute;left:70px;top:530px;width:140px;
    background:var(--white);border:3px solid var(--ink);
    font-family:"Noto Sans JP",sans-serif;font-weight:900;text-align:center;
    color:var(--ink);line-height:1.05;padding:8px 0;
  }
  .pack__spec b{display:block;font-size:46px}
  .pack__spec span{display:block;font-size:36px}
  .pack__script{
    position:absolute;right:70px;bottom:50px;white-space:nowrap;
    font-family:"Pinyon Script",cursive;font-size:160px;line-height:1;
    color:rgba(255,255,255,.8);text-shadow:0 2px 4px rgba(0,0,0,.15);
  }
</style>
</head>
<body>
<main class="sheet">

  <section class="pack pack--beef">
    <div class="pack__frame"></div>
    <svg class="pack__window" viewBox="0 0 800 360" aria-hidden="true">
      <path d="M40 4 H756 Q796 4 796 44 V316 Q796 356 756 356 H44 Q4 356 4 316 V44 Q4 4 40 4Z" fill="var(--window)" stroke="var(--window-edge)" stroke-width="8"/>
    </svg>
    <div class="pack__header">
      <p class="pack__tagline">お肉屋さんのこだわり食材</p>
      <div class="pack__animal" role="img" aria-label="牛のアイコン"></div>
      <h2 class="pack__name">牛ホルモン</h2>
      <p class="pack__size"><span class="pack__size-pill">使い切り</span>サイズ</p>
    </div>
    <div class="pack__series"><span>個食</span><span>パック</span><em>シリーズ</em></div>
    <div class="pack__spec"><b>100g</b><span>要冷凍</span></div>
    <p class="pack__script">Beef</p>
  </section>

  <section class="pack pack--pork">
    <div class="pack__frame"></div>
    <svg class="pack__window" viewBox="0 0 800 360" aria-hidden="true">
      <path d="M40 4 H756 Q796 4 796 44 V316 Q796 356 756 356 H44 Q4 356 4 316 V44 Q4 4 40 4Z" fill="var(--window)" stroke="var(--window-edge)" stroke-width="8"/>
    </svg>
    <div class="pack__header">
      <p class="pack__tagline">お肉屋さんのこだわり食材</p>
      <div class="pack__animal" role="img" aria-label="豚のアイコン"></div>
      <h2 class="pack__name">豚コマ切れ</h2>
      <p class="pack__size"><span class="pack__size-pill">使い切り</span>サイズ</p>
    </div>
    <div class="pack__series"><span>個食</span><span>パック</span><em>シリーズ</em></div>
    <div class="pack__spec"><b>100g</b><span>要冷凍</span></div>
    <p class="pack__script">Pork</p>
  </section>

  <section class="pack pack--chicken">
    <div class="pack__frame"></div>
    <svg class="pack__window" viewBox="0 0 800 360" aria-hidden="true">
      <path d="M40 4 H756 Q796 4 796 44 V316 Q796 356 756 356 H44 Q4 356 4 316 V44 Q4 4 40 4Z" fill="var(--window)" stroke="var(--window-edge)" stroke-width="8"/>
    </svg>
    <div class="pack__header">
      <p class="pack__tagline">お肉屋さんのこだわり食材</p>
      <div class="pack__animal" role="img" aria-label="鶏のアイコン"></div>
      <h2 class="pack__name">とりもも<small>(小)</small></h2>
      <p class="pack__size"><span class="pack__size-pill">使い切り</span>サイズ</p>
    </div>
    <div class="pack__series"><span>個食</span><span>パック</span><em>シリーズ</em></div>
    <div class="pack__spec"><b>100g</b><span>要冷凍</span></div>
    <p class="pack__script">Chicken</p>
  </section>

</main>
</body>
</html>
```